We need a web design for our business in which we provide complete network packages.

Hello Designers!

First, we’d like to make clear that rather than simple web design contents. We want someone that can help design our visual branding, help us communicate a sentiment. And we are willing to pay for that.

Who are we?

We are Harbor Lumen. Our company is based in Rotterdam, the Netherlands. We are providing a unique full-service concept for (wireless) communication networks within small to mid-range businesses. This means we will not only provide the hardware needed for a fast and secure network within a company, but will also install, optimize, support and maintain it. 

Harbor Lumen is a new brand of a company called Vector Lumen which has over 15 years of experience in the market of customer service and support. Harbor Lumen is the first satellite of more to come. Like Gear Lumen and others Planets, all have a focus on full service solutions.

Harbor Lumen has an experienced support center from which we can monitor our clients network in real time. Our clients don’t have to worry about anything, if something is not working correctly, we will fix it pro actively. Our clients range from education and training facilities, catering, industry, logistics, health care, consultancy agencies and high end consumers. 

In an overview all Unique Selling Points of Harbor Lumen:
• Professional service, both on location and remote!
• Direct clear price indication via our unique business configuration wizard
• A specific and complete quotation after a personal intake, within two days.
• Backed by a professional call center open 12 hours a day and open on Saturdays as well.
• Backed by a professional repair center with more than 15 years of experience.
• Installation and configuration included.
• Optimization included within the first three months powered by AI and machine learning.
• Real time remote maintenance. Quality control, security and interference.

Logo
For our business we need a logo. The logo needs to tell what we stand for and what we do. It will be used in both online and offline communication to our customers. Mainly e-mail and digital forms. As Harbor Lumen is one of the branches within our company we would like the logo to be part of a series in the future, which should be recognizable as part of a group of websites/brands.

Website
For our business we need a website.  The website needs a story and matching design and this is where you come in. The main focus of this website is to provide information, but more importantly to guide the user to our special quotation business configuration wizard. This business configuration wizard allows users to fill in information about their business and wish requirements, at which they will receive a real time price indication on completion. 

Configuration wizard
This business configuration wizard is developed separately by our own development team but should be part of the website in look and feel.. Our development team will develop the business configuration wizard and embed it in the website. 
The setup of the website should be focused on leading all visitors to the business configuration wizard which we create our quality leads. The website will inform the possible customers/leads on the unique selling points and then remind the customer to use the business configuration wizard to get a direct price indication. 

For the website and logo we need the whole package, the design you are creating needs to have returning elements like fonts, icons, color use,  images, maybe even characters etc. You name it! 
There needs to be a common thread in the design so we can reuse elements in, for example, the email templates, the work order or receipt we give to our customers (we may contact the winner of the contest to design these for us as well!). 

The layout needs to be complete. We want something modern. A one page design that is bright and colorful with collapsing area’s to show more information. 

Website wishes and requirements
The process:
The main function of our website, besides giving a clear indication what we do, will be to guide the user to our ‘business configuration wizard’. 

Website functionality:
Our website will be our main form of communication. We need a main/front page designed in a long single scrolling page style. Users can click on buttons to view more information. Information that was hidden before. We have included our own temporary mock ups to give you an idea of the flow we desire for the website. The titles and headers in these mock ups are in Dutch but we will translate this in the description below. These mock ups are just that, an idea about the visual presentation. You are free to implement your own design, fonts, icons, pictures etc.

The page will have 6 different areas (beside the top ‘hero’ part) and a final 7th area which is the “end page” and is a big business configuration wizard promotion.In each area you are pointed towards the business configuration wizard but if you scroll all the way down you will end up with this 7th area which is all about the wizard. However these 6 areas will need to be ‘expandable/collapsible’, meaning the user can click a “read more” button at which the element will expand to show extra information beneath it. The user can then collapse this element again by closing the part that just opened.

1. Top/Hero - Customers will be able to configure their own price indication through our wizard. So there will need to be a prominent button at the top of our main page and on the 7th area that will bring the customer to this wizard/application. This will need to be a focus throughout the whole website, meaning this button is a returning element. Furthermore the top needs two menus. One for navigating the main page itself, the other one is for switching between the different industry ‘flavors’ (Education, Logistics, Health Care etc). The idea is that the photos and text on the website will change depending on the industry picked. The design and layout remains the same however. The mock ups are based on ‘education’ and another based on logistics.

2. Real time Maintenance (Beheer) – This will be a collapsible component. It will provide a brief description of our maintenance service. The ‘configure now!’ button will need to be displayed in this area as well. This component is collapsible, meaning the user can click on a ‘Read more’ (Dutch: lees meer) button at which the element will open up to show extra information (2.1).
2.1 The extra information that can be collapsed by clicking the ‘X’ button. The headers on this page read “Carefree real time maintenance”, “Certified team of administrators”, “High service level”, “Defects immediately detected”, “Continuous remote maintenance”.

3.  Service range (Bereik) - This will be a collapsible component. It will provide a brief description of how we provide for enough wifi range within a building or company. The ‘configure now!’ button will need to be displayed in this area as well. This component is collapsible, meaning the user can click on a ‘Read more’ (Dutch: lees meer) button at which the element will open up to show extra information (3.1).
3.1 The extra information that can be collapsed by clicking the ‘X’ button. The headers on this page read “Enough range everywhere”, “Machine learning for maximum range”, “Different types of access points”, “Beamforming & Mu-MiMo”, “Multiple locations connected”.

4. Speed (Snelheid) -  This is the only component that needs to collapse twice. It will provide a brief description of how we will guarantee the fastest network speed possible. The ‘configure now!’ button will need to be displayed in this area as well. This component is collapsible, meaning the user can click on a ‘Read more’ (Dutch: lees meer) button at which the element will open up to show extra information (4.1).
4.1 The extra information that can be collapsed by clicking the ‘X’ button. The headers on this page read “Band steering, “Airtime fairness”, “Load balancing”. The user will be able to open up another element to show even more information (4.2).
4.2 This will mainly show the diagrams shown in the mock ups. It will provide extra information on what is meant by “Airtime fairness” and “Load balancing”.

5.  Manageable Costs (Beheersbare kosten) - This will be a collapsible component. It will provide a brief description of how users can manage their own costs. The ‘configure now!’ button will need to be displayed in this area as well. This component is collapsible, meaning the user can click on a ‘Read more’ (Dutch: lees meer) button at which the element will open up to show extra information (5.1).
5.1 The extra information that can be collapsed by clicking the ‘X’ button. The headers on this page read “Manageable costs”, “Upfront insight in predicated costs”, “Best price/quality ratio”, “10 years of warranty”, “High availability”.

6.  Protected and secure (Beschermd en veilig) -  This will be a collapsible component. It will provide a brief description of our protection and security guaranties. The ‘configure now!’ button will need to be displayed in this area as well. This component is collapsible, meaning the user can click on a ‘Read more’ (Dutch: lees meer) button at which the element will open up to show extra information (6.1).
6.1 The extra information that can be collapsed by clicking the ‘X’ button. The headers on this page read “Protected and Secure”, “Protected by Kelvo”, “Fire resistant and dust free”, “Managed and maintained in the Netherlands”.

7. Extras (Extra’s) - This will be a collapsible component. It will provide a brief description of additional options which our solution can provide. The ‘configure now!’ button will need to be displayed in this area as well. This component is collapsible, meaning the user can click on a ‘Read more’ (Dutch: lees meer) button at which the element will open up to show extra information (7.1).
7.1 The extra information that can be collapsed by clicking the ‘X’ button. The headers on this page read “Connection with portals like Chatloom”, “Everything in one cable”, “Cloud ready”, “Ready for even more?”.

8. unique business configuration wizard - This is the final page to (once again!) push the visitor to the ‘configure now!’ button showing some reasons to click right now.

For now, we need a logo and a website designed. We would also like a design for the configuration wizard in the same style as the website.

What we'd like:
- A modern professional, but fun, appearance
- Elements like icons to have a flat design.
- Website can be used for the different industry flavors (for example, our mockups are geared towards clients in the education sector, but we can simply swap some of the photos and content to reflect the health care sector).
- Keep in mind that the website will need to be responsive when designing!
- Create a fun and trustworthy feeling.

We will be able to provide stock photographs if necessary!

```html
<!DOCTYPE html>
<html lang="nl">
<head>
<meta charset="utf-8">
<title>Harbor Lumen – beheerde draadloze netwerken</title>
<link rel="stylesheet" href="https://fonts.googleapis.com/css2?family=Poppins:wght@500;600;700&family=Questrial&family=Lato:wght@700;900&display=swap">
<style>
  :root {
    --ink: #000000;
    --white: #ffffff;
    --red: #e8262d;
    --grey-disc: #2b2b2b;
    --ring: #3a3a3a;
    --muted: #d8d8d8;
    --nav-dim: #bfbfbf;
  }
  * { box-sizing: border-box; margin: 0; padding: 0; }
  html, body { width: 711px; height: 1200px; overflow: hidden; background: var(--ink); }
  .page { position: relative; width: 711px; height: 1200px; overflow: hidden; background: var(--ink); color: var(--white); font-family: "Questrial", sans-serif; }
  .abs { position: absolute; }

  /* hero */
  .hero { left: 0; top: 0; width: 711px; height: 418px;
    background: radial-gradient(ellipse at 50% 45%, #6b6a70 0%, #3d3a3c 35%, #1f1c1c 70%, #000 100%); }
  .hero-fade { left: 0; top: 300px; width: 711px; height: 120px; background: linear-gradient(to bottom, rgba(0,0,0,0), #000); }
  .industry-nav { left: 52px; top: 13px; display: flex; gap: 7.5px; align-items: baseline; font-family: "Lato", sans-serif; font-weight: 700; font-size: 4.6px; letter-spacing: 0.1px; color: var(--nav-dim); }
  .industry-nav .current { font-size: 6.2px; color: var(--white); font-weight: 900; }
  .brand-mark { left: 343px; top: 9px; display: flex; align-items: center; gap: 3px; font-family: "Poppins", sans-serif; font-weight: 600; font-size: 6px; color: var(--white); }
  .brand-mark .dot { width: 8px; height: 8px; border-radius: 50%; background: var(--white); }
  .page-nav { left: 410px; top: 12px; width: 249px; display: flex; justify-content: space-between; font-family: "Lato", sans-serif; font-weight: 700; font-size: 6.7px; }
  .hero-title { left: 200px; top: 178px; width: 256px; text-align: right; font-family: "Poppins", sans-serif; font-weight: 600; font-size: 27px; line-height: 1; }
  .hero-tagline { left: 200px; top: 208px; width: 256px; text-align: right; font-size: 8px; line-height: 9.6px; color: var(--muted); }
  .hero-tagline em { font-style: normal; color: var(--red); }

  /* configure button */
  .cta { display: flex; align-items: center; gap: 8px; font-family: "Poppins", sans-serif; font-weight: 600; color: var(--white); white-space: nowrap; }
  .cta svg { flex: none; }
  .cta-hero { left: 257px; top: 333px; font-size: 22px; }
  .cta-right { right: 52px; top: 737px; font-size: 21px; }
  .cta-bottom { right: 52px; top: 1137px; font-size: 21px; }

  /* sections */
  .section-title { font-family: "Poppins", sans-serif; font-weight: 600; font-size: 18px; color: var(--red); line-height: 1; }
  .section-heading { font-family: "Poppins", sans-serif; font-weight: 600; font-size: 14px; line-height: 1; }
  .copy { font-size: 6.9px; line-height: 8.15px; color: var(--muted); }
  .copy p + p { margin-top: 8px; }
  .copy-right { text-align: right; }
  .read-more { font-family: "Poppins", sans-serif; font-weight: 500; font-size: 10.5px; color: var(--red); }

  .disc { border-radius: 50%; background: var(--grey-disc); }
  .photo-ring { left: 0; top: 473px; width: 274px; height: 274px; border-radius: 50%; background: var(--ring); }
  .photo-circle { left: 8px; top: 481px; width: 258px; height: 258px; border-radius: 50%;
    background: linear-gradient(160deg, #b4563c 0%, #5d6f80 35%, #d9e3e6 60%, #2c3a52 100%); }
  .feature { font-family: "Lato", sans-serif; font-weight: 900; font-size: 6.2px; letter-spacing: 0.05px; }
  .leader { stroke: var(--ink); stroke-width: 0.8; }

  .reach-bg { left: 0; top: 805px; width: 711px; height: 395px;
    background: linear-gradient(to bottom, #000 0%, #2a2623 18%, #3a3531 50%, #2b2725 100%); }
  .class-photo { left: 409px; top: 912px; width: 250px; height: 171px;
    background: linear-gradient(135deg, #8fb7a6 0%, #6d7a74 40%, #3e3d46 75%, #7c5a60 100%); }
</style>
</head>
<body>
<main class="page">

  <!-- hero -->
  <div class="abs hero" role="img" aria-label="Foto van bovenaf: handen van studenten rond een laptop op een tafel"></div>
  <div class="abs hero-fade"></div>

  <nav class="abs industry-nav">
    <span class="current">ONDERWIJS</span><span>LOGISTIEK</span><span>INDUSTRIE</span><span>KANTOOR</span><span>GEZONDHEIDSZORG</span><span>RESTAURANT</span><span>VILLA</span>
  </nav>
  <div class="abs brand-mark"><span class="dot"></span>Harbor Lumen</div>
  <nav class="abs page-nav">
    <span>Beheer</span><span>Bereik</span><span>Snelheid</span><span>kosten</span><span>veilig</span><span>extras</span>
  </nav>

  <h1 class="abs hero-title">Harbor Lumen</h1>
  <p class="abs hero-tagline">beheerde draadloze netwerken<br>voor het <em>ONDERWIJS</em></p>

  <a class="abs cta cta-hero">
    <svg width="30" height="30" viewBox="0 0 30 30" aria-hidden="true">
      <circle cx="15" cy="15" r="14" fill="#e8262d"/>
      <path d="M15 7 L21 14 H17 V22 H13 V14 H9 Z" fill="#fff"/>
    </svg>
    configureer nu!
  </a>

  <!-- beheer -->
  <h2 class="abs section-title" style="left:52px;top:430px;">Beheer</h2>
  <h3 class="abs section-heading" style="right:52px;top:433px;">zorgeloos realtime beheer</h3>

  <div class="abs disc" style="left:16px;top:441px;width:44px;height:44px;"></div>
  <div class="abs photo-ring"></div>
  <div class="abs photo-circle" role="img" aria-label="Foto van een laptop met een dashboard vol grafieken"></div>
  <div class="abs disc" style="left:290px;top:592px;width:27px;height:27px;"></div>
  <div class="abs disc" style="left:17px;top:689px;width:50px;height:50px;"></div>

  <svg class="abs" style="left:0;top:0;" width="711" height="700" aria-hidden="true">
    <g class="leader">
      <line x1="154" y1="567" x2="227" y2="567"/><circle cx="154" cy="567" r="1.3" fill="#000"/>
      <line x1="212" y1="581" x2="227" y2="581"/><circle cx="212" cy="581" r="1.3" fill="#000"/>
      <line x1="123" y1="646" x2="227" y2="646"/><circle cx="123" cy="646" r="1.3" fill="#000"/>
      <line x1="194" y1="656" x2="227" y2="656"/><circle cx="194" cy="656" r="1.3" fill="#000"/>
    </g>
  </svg>
  <span class="abs feature" style="left:227px;top:564px;">CONTINUE BEHEER OP AFSTAND</span>
  <span class="abs feature" style="left:227px;top:578px;">GECERTIFICEERD TEAM AAN BEHEERDERS</span>
  <span class="abs feature" style="left:227px;top:643px;">HOOG SERVICE NIVEAU</span>
  <span class="abs feature" style="left:227px;top:653px;">DEFECTEN GELIJK GEDETECTEERD</span>

  <div class="abs copy copy-right" style="left:400px;top:495px;width:259px;">
    <p>Lorem ipsum dolor sit amet, consetetur sadipscing elitr, sed diam nonumy eirmod tempor invidunt ut labore et dolore magna aliquyam erat, sed diam voluptua. At vero eos et accusam et justo duo dolores et ea rebum. Stet clita kasd gubergren, no sea takimata sanctus est Lorem ipsum dolor sit amet. Lorem ipsum dolor sit amet, consetetur sadipscing elitr, sed diam nonumy eirmod tempor invidunt ut labore et dolore magna aliquyam erat, sed diam voluptua. At vero eos et accusam et justo duo dolores et ea rebum. Stet clita kasd gubergren, no sea takimata sanctus est Lorem ipsum dolor sit amet.</p>
    <p>Lorem ipsum dolor sit amet, consetetur sadipscing elitr, sed diam nonumy eirmod tempor invidunt ut labore et dolore magna aliquyam erat, sed diam voluptua. At vero eos et accusam et justo duo dolores et ea rebum. Stet clita kasd gubergren, no sea takimata sanctus est Lorem ipsum dolor sit amet. Lorem ipsum dolor sit amet, consetetur sadipscing elitr, sed diam nonumy eirmod tempor invidunt ut labore et dolore magna aliquyam erat, sed diam voluptua. At vero eos et accusam et justo duo dolores et ea rebum. Stet clita kasd gubergren, no sea takimata sanctus est Lorem ipsum dolor sit ame</p>
  </div>
  <a class="abs read-more" style="right:52px;top:678px;">+ Lees Meer</a>

  <a class="abs cta cta-right">
    <svg width="30" height="30" viewBox="0 0 30 30" aria-hidden="true">
      <circle cx="15" cy="15" r="14" fill="#e8262d"/>
      <path d="M15 7 L21 14 H17 V22 H13 V14 H9 Z" fill="#fff"/>
    </svg>
    configureer nu!
  </a>

  <!-- bereik -->
  <div class="abs reach-bg" role="img" aria-label="Foto van bovenaf: werktafel met laptops, koffie, kabels en telefoons"></div>
  <h2 class="abs section-title" style="left:52px;top:838px;">Bereik</h2>
  <h3 class="abs section-heading" style="left:52px;top:905px;">overal voldoende bereik</h3>

  <div class="abs copy" style="left:52px;top:968px;width:259px;">
    <p>Lorem ipsum dolor sit amet, consetetur sadipscing elitr, sed diam nonumy eirmod tempor invidunt ut labore et dolore magna aliquyam erat, sed diam voluptua. At vero eos et accusam et justo duo dolores et ea rebum. Stet clita kasd gubergren, no sea takimata sanctus est Lorem ipsum dolor sit amet. Lorem ipsum dolor sit amet, consetetur sadipscing elitr, sed diam nonumy eirmod tempor invidunt ut labore et dolore magna aliquyam erat, sed diam voluptua. At vero eos et accusam et justo duo dolores et ea rebum. Stet clita kasd gubergren, no sea takimata sanctus est Lorem ipsum dolor sit amet.</p>
    <p>Lorem ipsum dolor sit amet, consetetur sadipscing elitr, sed diam nonumy eirmod tempor invidunt ut labore et dolore magna aliquyam erat, sed diam voluptua. At vero eos et accusam et justo duo dolores et ea rebum. Stet clita kasd gubergren, no sea takimata sanctus est Lorem ipsum dolor sit amet. Lorem ipsum dolor sit amet, consetetur sadipscing elitr, sed diam nonumy eirmod tempor invidunt ut labore et dolore magna aliquyam erat, sed diam voluptua. At vero eos et accusam et justo duo dolores et ea rebum. Stet clita kasd gubergren, no sea takimata sanctus est Lorem ipsum dolor sit ame</p>
  </div>
  <a class="abs read-more" style="left:52px;top:1152px;">Lees Meer +</a>

  <div class="abs class-photo" role="img" aria-label="Foto van een klaslokaal met leerlingen en een docent voor het bord"></div>

  <a class="abs cta cta-bottom">
    <svg width="30" height="30" viewBox="0 0 30 30" aria-hidden="true">
      <circle cx="15" cy="15" r="14" fill="#e8262d"/>
      <path d="M15 7 L21 14 H17 V22 H13 V14 H9 Z" fill="#fff"/>
    </svg>
    configureer nu!
  </a>

</main>
</body>
</html>
```